Landing Page IT Security Vendor

We need a landing page that uses our colour scheme (www.veldonguard.com). We created a draft (see attached). We do not need standard stock template design pages. Please only apply if you can design pages from scratch and try to be as close as possible to our draft. It is ok to also purchase commecrial stock pictures

Coding

Coded - Design and coding required

Number of Pages Required

1 page

```html
<!DOCTYPE html>
<html lang="en">
<head>
<meta charset="utf-8">
<title>Veldon – Cyber Security Awareness Training</title>
<link href="https://fonts.googleapis.com/css2?family=Poppins:wght@300;400;500;600;700;800&display=swap" rel="stylesheet">
<style>
:root{
  --teal:#1cc0cc;
  --teal-deep:#13a9b6;
  --teal-light:#4fd3da;
  --orange:#f8a51b;
  --orange-deep:#e38c0c;
  --ink:#111;
  --grey:#666;
  --line:#e2e2e2;
  --white:#fff;
  --mist:#eef0f0;
}
*{margin:0;padding:0;box-sizing:border-box}
html,body{width:1200px;height:2315px;overflow:hidden}
body{font-family:'Poppins',sans-serif;color:var(--ink);background:var(--white);position:relative}
.abs{position:absolute}
.bg{position:absolute;left:0;top:0}
.brand{display:flex;align-items:center;gap:8px;font-weight:800;font-size:30px;color:var(--ink)}
.brand .dot{width:30px;height:30px;border-radius:50%;background:var(--orange)}
.nav{left:270px;top:100px;display:flex;font-size:14px;color:var(--ink)}
.nav a{color:inherit;text-decoration:none;margin-right:47px}
.hero-kicker{left:66px;top:195px;font-size:26px;font-weight:600;letter-spacing:.5px;white-space:nowrap}
.hero-title{left:66px;top:242px;font-size:47px;line-height:57px;font-weight:800;color:var(--white);width:720px;white-space:nowrap}
.btn{display:flex;align-items:center;justify-content:center;border-radius:24px;background:var(--orange);color:var(--white);font-size:12.5px;font-weight:600;height:42px;white-space:nowrap}
.photo{background:linear-gradient(160deg,#2b2b2b 0%,#e9a22e 35%,#f0b03c 60%,#e8e8e8 100%);border-radius:40% 40% 8px 8px}
.help{left:0;width:1200px;top:575px;text-align:center;font-size:30px;font-weight:700}
.card{top:654px;width:322px;height:447px;background:var(--white);border-radius:16px;box-shadow:0 8px 30px rgba(0,0,0,.06);text-align:center;padding:0 26px}
.card h3{color:var(--orange);font-size:19px;font-weight:700;line-height:27px;height:130px;padding-top:8px;display:flex;align-items:center;justify-content:center;white-space:nowrap}
.card .lead{font-size:12.3px;font-weight:500;line-height:20.6px;padding:0 16px}
.card .body{font-size:12.3px;font-weight:300;color:var(--grey);line-height:20.6px;margin-top:20px}
.card .btn{position:absolute;left:85px;bottom:37px;width:152px}
.mssp{left:0;top:1172px;width:1200px;height:128px;background:linear-gradient(90deg,var(--orange-deep),var(--orange) 70%)}
.mssp-text{left:70px;top:1212px;font-size:30px;font-weight:700;color:var(--white);white-space:nowrap}
.btn-white{background:var(--white);color:var(--ink);font-weight:500}
.client{display:flex;align-items:center;justify-content:center;font-weight:700;font-size:22px}
.trust-title{left:627px;top:1458px;font-size:31px;font-weight:700;line-height:42px;width:540px;white-space:nowrap}
.trust-title .hl{color:var(--teal)}
.trust-copy{left:627px;top:1605px;width:520px;font-size:12.3px;color:var(--grey);line-height:20.6px}
.trust-copy p{margin-bottom:20px}
.footer-head{left:66px;top:1995px;font-size:22px;font-weight:600;color:var(--white)}
.fcol{top:2050px;font-size:12.3px;line-height:20.6px;color:var(--white);white-space:nowrap}
.rights{left:958px;top:2016px;font-size:12.3px;color:#333}
.divider{left:66px;top:2193px;width:1068px;height:1px;background:rgba(255,255,255,.5)}
.badges{left:57px;top:2213px;width:615px;height:70px;background:var(--teal-deep);display:flex;align-items:center;justify-content:space-around;padding:0 8px}
.badges span{width:48px;height:48px;background:rgba(255,255,255,.85)}
.badges span.round{border-radius:50%}
.lang{left:880px;top:2233px;font-size:21px;font-weight:600;color:var(--white)}
.select{left:1005px;top:2228px;width:126px;height:42px;border-radius:22px;background:var(--white);font-size:12.5px;color:#333;display:flex;align-items:center;justify-content:space-between;padding:0 20px 0 22px}
</style>
</head>
<body>

<svg class="bg" width="1200" height="2315" viewBox="0 0 1200 2315" aria-hidden="true">
  <path d="M0 0 H660 C700 40 780 50 850 25 C900 5 960 0 1050 0 H1200 V630 C1150 690 1080 700 1000 660 C900 610 820 650 700 660 C560 670 460 620 330 600 C200 580 90 600 0 615 Z" fill="var(--teal)"/>
  <path d="M0 540 C120 520 220 560 330 600 L0 620 Z" fill="var(--teal-light)" opacity=".5"/>
  <path d="M700 1300 C680 1360 700 1410 760 1420 C880 1440 960 1390 1060 1440 C1120 1470 1160 1500 1200 1500 V1300 Z" fill="var(--mist)"/>
  <path d="M0 1760 C40 1800 60 1850 60 1900 L0 1900 Z" fill="var(--mist)"/>
  <path d="M0 1910 C180 1960 320 1880 480 1900 C640 1920 760 1990 900 1990 C1040 1990 1120 1900 1200 1860 V2315 H0 Z" fill="var(--teal)"/>
  <path d="M0 1960 C200 1990 380 1930 560 1960 C700 1985 820 2050 980 2040 L1200 2020 V2315 H0 Z" fill="var(--teal-light)" opacity=".35"/>
  <path d="M960 1930 C1040 1900 1120 1880 1200 1870 V2060 C1140 2060 1080 2050 1020 2030 Z" fill="var(--white)"/>
</svg>

<header>
  <div class="abs brand" style="left:63px;top:90px"><span class="dot"></span>Veldon</div>
  <nav class="abs nav"><a>Home</a><a>Solution</a><a>Pricing</a><a>Resources</a><a>About</a></nav>
</header>

<section class="hero">
  <div class="abs photo" role="img" aria-label="Smiling woman in a yellow top holding a tablet" style="left:760px;top:55px;width:300px;height:600px"></div>
  <div class="abs hero-kicker">Cyber Security Starts with People</div>
  <h1 class="abs hero-title">Train Your Staff with<br>Veldon and Improve Cyber<br>Security Awareness</h1>
  <div class="abs btn" style="left:66px;top:448px;width:152px">Request a Demo</div>
</section>

<section class="services">
  <h2 class="abs help">How can We help?</h2>
  <article class="abs card" style="left:66px">
    <h3>Important Our Training<br>Courses In Your LMS</h3>
    <p class="lead">Buy out of the box or custom tailored security courses you can import in your elearning (SCORM)</p>
    <p class="body">Veldon offers 250 fully customizable training modules in +30 languages. Games, videos, exams, posters, offline, micro-training and much more!</p>
    <div class="btn">Explore Training</div>
  </article>
  <article class="abs card" style="left:439px">
    <h3>Let us Develop a Security<br>Awareness Program</h3>
    <p class="lead">Veldon Guard will assist you in improving security awareness - with money back guarantee!</p>
    <p class="body">Our security awareness specialists will identify risky users via phishing simulations. We develop a tailored awareness program and reduce your exposure to social hacking.</p>
    <div class="btn">Explore Services</div>
  </article>
  <article class="abs card" style="left:811px">
    <h3>Install the Veldon Software<br>on-premise or get access<br>to the SAAS Version</h3>
    <p class="lead">You want to run the campaign yourself? Choose your prefered setup type and get started in 24h!</p>
    <p class="body">The Veldon software can be installed on-premise or in the cloud. If you don't want to deal with the installation we onboard you in 24 h on our SaaS!</p>
    <div class="btn">Explore Software</div>
  </article>
</section>

<section>
  <div class="abs mssp"></div>
  <div class="abs mssp-text">Veldon is also available for MSSP</div>
  <div class="abs btn btn-white" style="left:661px;top:1212px;width:153px">Learn More</div>
  <div class="abs photo" role="img" aria-label="Smiling woman leaning on a sofa with a tablet" style="left:910px;top:1132px;width:180px;height:168px;border-radius:50% 50% 0 0;background:linear-gradient(160deg,#3a2a22,#8a7a80 60%,#5a5a60)"></div>
</section>

<section class="clients">
  <div class="abs" style="left:320px;top:1385px;width:1px;height:487px;background:var(--line)"></div>
  <div class="abs" style="left:113px;top:1542px;width:412px;height:1px;background:var(--line)"></div>
  <div class="abs" style="left:113px;top:1714px;width:412px;height:1px;background:var(--line)"></div>
  <div class="abs client" style="left:113px;top:1400px;width:207px;height:130px;color:#1d2d8f">Norvane</div>
  <div class="abs client" style="left:321px;top:1400px;width:204px;height:130px;color:#e1151b">Railmark</div>
  <div class="abs client" style="left:113px;top:1560px;width:207px;height:140px;color:#d8222a">Hausfeld</div>
  <div class="abs client" style="left:321px;top:1560px;width:204px;height:140px;color:#e1151b">Kestrel Works</div>
  <div class="abs client" style="left:113px;top:1730px;width:207px;height:120px;color:#0f7f6e">Tannick</div>
  <div class="abs client" style="left:321px;top:1730px;width:204px;height:120px;color:#1e2c7a">Aerolux</div>

  <h2 class="abs trust-title">Already over <span class="hl">12’000’000</span><br>Employees worldwide trust<br>and use Veldon.</h2>
  <div class="abs trust-copy">
    <p>Veldon Guard is a name you can trust! Because we have won countless awards since 2015 and help well-known brands around the world.</p>
    <p>You know you're getting a quality solution with us.</p>
    <p>Our services can be customized to fit your needs and company size.<br>Talk to our team today to learn more.</p>
  </div>
  <div class="abs btn" style="left:626px;top:1784px;width:310px">Get in Contact with the Veldon Team Now!</div>
</section>

<footer>
  <div class="abs brand" style="left:965px;top:1966px"><span class="dot"></span>Veldon</div>
  <div class="abs rights">ll Rights Reserved 2020</div>
  <h3 class="abs footer-head">Contacts</h3>
  <div class="abs fcol" style="left:66px">Address: North America<br>Veldon Guard USA<br>4410 Meridian Ave<br>Suite 300<br>Austin, TX 78701</div>
  <div class="abs fcol" style="left:262px">Phone Global: +41 44 000 12 34<br>Phone USA: +1-512-555-0142<br>Phone USA Support: +1-512-555-0178<br>Phone France: +33 600 000 417<br>Phone UK: +44 (0) 7700 900318</div>
  <div class="abs fcol" style="left:525px">Address: Europe<br>Veldon Guard AG<br>Seeweg 12 | 6300 Zug | Switzerland</div>
  <div class="abs divider"></div>
  <div class="abs badges">
    <span></span><span class="round"></span><span></span><span></span><span></span><span></span><span></span><span></span><span class="round"></span><span class="round"></span>
  </div>
  <div class="abs lang">Language</div>
  <div class="abs select">English <svg width="8" height="5" viewBox="0 0 8 5"><path d="M1 1l3 3 3-3" stroke="#333" fill="none"/></svg></div>
</footer>

</body>
</html>
```